we are an outdoor outlet in a country club that has a variety of outlets. The Club is called Lanterns and is located in Cairo, Egypt. This garden menu will include cuisines from the Mediterranean, Asia and Texmex. we need a menu that is colorful and would fit an A3 size, back and front are to be used. Attached is the old menu currently in use (Garden Menu 2012.pdf is just for reference) and the new menu text for you to use is under the name Garden Menu Fall 2013
thank you.

```html
<!DOCTYPE html>
<html lang="en">
<head>
<meta charset="UTF-8">
<title>Garden Menu</title>
<link href="https://fonts.googleapis.com/css2?family=Cabin+Sketch:wght@700&family=Luckiest+Guy&family=PT+Serif:wght@700&display=swap" rel="stylesheet">
<style>
  :root {
    --leaf-green: #a0dd8a;
    --tangerine: #fdb459;
    --ink: #111111;
    --cream: #ffffff;
    --soup-red: #9c2a1c;
    --appetizer-violet: #b74ee0;
    --doodle-yellow: #f6ef5a;
    --doodle-pink: #e7a6c8;
    --doodle-violet: #c9a8ea;
  }
  html, body {
    margin: 0;
    padding: 0;
    overflow: hidden;
  }
  .menu-page {
    position: relative;
    width: 848px;
    height: 1200px;
    background: var(--tangerine);
    overflow: hidden;
  }
  .side-band {
    position: absolute;
    left: 0;
    top: 0;
    width: 280px;
    height: 1200px;
    background: var(--leaf-green);
    border-right: 3px solid var(--ink);
    box-sizing: border-box;
  }
  .garden-doodles {
    position: absolute;
    left: 0;
    top: 165px;
    width: 277px;
    height: 1035px;
    background: linear-gradient(180deg,
      var(--leaf-green) 0%,
      var(--doodle-yellow) 18%,
      var(--doodle-violet) 40%,
      var(--doodle-pink) 62%,
      var(--doodle-yellow) 80%,
      var(--doodle-pink) 100%);
    opacity: 0.75;
  }
  .menu-column {
    position: absolute;
    left: 280px;
    right: 0;
    top: 0;
    bottom: 0;
    text-align: center;
    color: var(--cream);
  }
  .menu-column > * {
    position: absolute;
    left: 0;
    right: 0;
    margin: 0;
  }
  .menu-title {
    top: 52px;
    font-family: "Cabin Sketch", cursive;
    font-weight: 700;
    font-size: 50px;
    letter-spacing: 1px;
    line-height: 1;
  }
  .section-heading {
    font-family: "Luckiest Guy", cursive;
    font-weight: 400;
    font-size: 22px;
    letter-spacing: 0.5px;
    line-height: 1;
  }
  .section-heading--soups { top: 161px; color: var(--soup-red); }
  .section-heading--appetizers { top: 467px; color: var(--appetizer-violet); }
  .dish {
    font-family: "PT Serif", serif;
    font-weight: 700;
    font-size: 17px;
    line-height: 21.3px;
  }
</style>
</head>
<body>
<div class="menu-page">
  <div class="side-band">
    <div class="garden-doodles" role="img" aria-label="Colourful hand-drawn garden doodles: a sun, swirls, a butterfly, a tree, flowers, sparkles and a heart"></div>
  </div>

  <div class="menu-column">
    <h1 class="menu-title">GARDEN MENU</h1>

    <h2 class="section-heading section-heading--soups">MEDITERRANEAN CORNER SOUPS:</h2>
    <p class="dish" style="top:204px">Tomato Basil<br>Simmered tomato soup finished<br>with fresh basil and cream</p>
    <p class="dish" style="top:288px">Chicken Cream<br>Chicken broth with roasted chicken cubes,<br>pine nuts, and cream</p>
    <p class="dish" style="top:372px">Moroccan Harira<br>Vegetable broth with fresh tomato,<br>chickpeas, lentil, cilantro, and diced lamb</p>

    <h2 class="section-heading section-heading--appetizers">APPETIZERS:</h2>
    <p class="dish" style="top:515px">Salmon tartare seasoned with<br>lemon juice, garlic, and crushed black pepper</p>
    <p class="dish" style="top:577px">Roasted eggplant rolls with<br>herbed ricotta cheese and pine nuts</p>
    <p class="dish" style="top:640px">Falafel in mini pita served<br>with tehina and oriental salsa</p>
    <p class="dish" style="top:701px">Mankousha with thyme and olive oil</p>
    <p class="dish" style="top:743px">Fried kobeba with minced meat,<br>spices, and pine nuts</p>
    <p class="dish" style="top:803px">Fried calamari a la Romana served with aioli<br>Samboussek with herbed white cheese and mint</p>
    <p class="dish" style="top:867px">Oriental sausage sautéed with garlic and onion<br>Mini vine leaves with a yoghurt dip</p>
    <p class="dish" style="top:928px">Fatouch with a pomegranate<br>syrup dressing Hummus seasoned with<br>lemon juice, garlic, and olive oil</p>
    <p class="dish" style="top:1011px">White cheese with diced tomato, thyme,<br>and olive oil Tehina seasoned with cumin,<br>lemon juice, and garlic</p>
  </div>
</div>
</body>
</html>
```